Web Site Design For Real Estate Sales Project

The idea behind this project is pretty simple. I am putting my penthouse apartment up for sale and am trying to be creative in selling it.
Technically this will be pretty simple, it will be 3 pages but graphically this has to be as impressive as possible which is why I am trying Pixel Harbor.
The apartment is located in Barra Da Tijuca, Rio De Janeiro, Brazil. (This is where the 2016 Meridian Regatta will be held)
I am looking for an index page and 2 sub-pages. I am open to all kinds of designs and navigation's but it has to make an impression quickly with a professional and enticing design. The index page should make it obvious that there is a penthouse apartment for sale in Barra Da Tijuca ( suburb of Rio De Janeiro). The first sub page is about the Condominium where the apartment is located, the second sub page is about the apartment itself.
Here is a more detailed description of what the 3 pages should be about.
Index Page
This is the landing page and should make it obvious that there is an apartment for sale in Barra Da Tijuca, Rio De Janeiro with the following attributes
251 SQ M
Duplex Penthouse
4 suites
Price R$ 2.200.000
Price per SQ M: R$ 8.764
First Sub-Page
This is about the Condominium which is called "Gentle Palm Residences" with the following bullets
*Family friendly and safe
*Direct access to the beach
*Many amenities like pool, football court, gym, sauna
There should be some photos of the condominium and a link to the site of the condominium ( www.gprvx.com )
Second Sub-page
This is about the apartment. It should list in bullets the features of the apartment and then have a photo gallery of the view and various rooms. I have attached sample photos but will eventually have to use more photos.
Apartment Features
Price: R$ 2.220.000
251 m2 Duplex Penthouse
4 suites
maids room with bath
guest bathroom
living room
dinning room
Terrace with heated pool for year round use
Veranda
As mentioned above I am open to all designs and navigation so feel free to be creative. The important thing is catch peoples attention and get the message across in a few seconds, which is that there is an apartment for sale at this price with these features in this location. I will then use brightlist promoter and SEO to get people to the site.
Thanks
Target Market(s)
Men and Women from 30-60 years of age.
Industry/Entity Type
Apartment

```html
<!DOCTYPE html>
<html lang="en">
<head>
<meta charset="utf-8">
<title>Penthouse for Sale – Barra da Tijuca</title>
<link rel="stylesheet" href="https://fonts.googleapis.com/css2?family=Source+Sans+3:ital,wght@0,400;0,600;0,700;1,400;1,600;1,700&family=Open+Sans:wght@500;700&display=swap">
<style>
  :root {
    --sky-top: #a9cde6;
    --sky-mid: #cfe4f2;
    --white: #ffffff;
    --ink: #444444;
    --ink-soft: #555555;
    --nav-ink: #3c3c3c;
    --rule: #b9b9b9;
    --band: #ebebea;
    --band-edge: #d8d8d6;
    --brown: #7b3a1c;
    --green: #5b6f1e;
    --ring: #9ec0e0;
    --wood: #a06a3e;
    --wood-dark: #6e4526;
    --grass: #3f6a24;
  }
  * { box-sizing: border-box; margin: 0; padding: 0; }
  html, body { width: 993px; height: 1200px; overflow: hidden; }
  body {
    position: relative;
    font-family: "Source Sans 3", "Myriad Pro", sans-serif;
    color: var(--ink);
    background: var(--white);
  }
  .sky {
    position: absolute; left: 0; top: 0; width: 993px; height: 600px;
    background: linear-gradient(180deg, var(--sky-top) 0%, var(--sky-mid) 40%, #eef5fa 75%, var(--white) 100%);
  }
  .phone {
    position: absolute; right: 120px; top: 10px;
    color: var(--white); font-style: italic; font-weight: 700; font-size: 16px;
    text-shadow: 0 1px 2px rgba(0,0,0,.35);
  }
  .header-bar {
    position: absolute; left: 0; top: 37px; width: 993px; height: 59px;
    background: rgba(255,255,255,.93);
    box-shadow: 0 6px 18px rgba(255,255,255,.8);
  }
  .logo {
    position: absolute; left: 189px; top: 48px;
    font-family: "Open Sans", sans-serif; font-weight: 700; font-size: 34px;
    color: #4a4a4a; letter-spacing: .5px;
  }
  .main-nav {
    position: absolute; left: 498px; top: 56px;
    display: flex; align-items: center; gap: 24px;
    font-family: "Open Sans", sans-serif; font-weight: 500; font-size: 14px;
    color: var(--nav-ink); letter-spacing: .3px;
  }
  .main-nav svg { display: block; margin-right: -4px; }
  .signpost {
    position: absolute; left: 135px; top: 168px; width: 210px; height: 402px;
    border-radius: 8px;
    background: linear-gradient(180deg, rgba(160,106,62,.0) 0%, rgba(160,106,62,.35) 10%, rgba(160,106,62,.55) 50%, rgba(110,69,38,.35) 82%, rgba(63,106,36,.75) 100%);
  }
  .signpost span {
    position: absolute; left: 0; width: 100%; text-align: center;
    font-style: italic; font-weight: 700; color: #4a2d16; text-transform: uppercase;
  }
  .sign-sale { top: 56px; font-size: 19px; }
  .sign-1 { top: 118px; font-size: 21px; }
  .sign-2 { top: 160px; font-size: 21px; }
  .sign-3 { top: 203px; font-size: 21px; }
  .gallery-main {
    position: absolute; left: 394px; top: 183px; width: 494px; height: 330px;
    border: 3px solid var(--white);
    box-shadow: 0 0 3px rgba(0,0,0,.25);
    background: linear-gradient(180deg, #e9e7e2 0%, #d8d2c8 45%, #7a3e26 70%, #3c1c10 100%);
  }
  .gallery-strip {
    position: absolute; left: 428px; top: 522px; width: 425px; height: 46px;
  }
  .arrow-btn { position: absolute; top: 3px; }
  .thumb {
    position: absolute; top: 2px; height: 44px;
    border: 2px solid var(--white); box-shadow: 0 0 2px rgba(0,0,0,.3);
  }
  .t1 { left: 56px; width: 64px; background: linear-gradient(180deg,#d9d6d0,#5a3a2a); }
  .t2 { left: 137px; width: 64px; background: linear-gradient(180deg,#cfcac2,#4d3427); }
  .t3 { left: 218px; width: 66px; background: linear-gradient(180deg,#b9c6d0,#2f6f8f); }
  .t4 { left: 304px; width: 66px; background: linear-gradient(180deg,#e5e3df,#7a5644); }
  .welcome-title {
    position: absolute; left: 132px; top: 619px; width: 714px;
    display: flex; align-items: center; gap: 14px;
    font-style: italic; font-weight: 600; font-size: 20px; color: #4a4a4a;
  }
  .welcome-title::before, .welcome-title::after {
    content: ""; flex: 1; height: 1px; background: var(--rule);
  }
  .welcome-text {
    position: absolute; left: 128px; top: 652px; width: 722px;
    text-align: center; font-style: italic; font-size: 16.2px; line-height: 19.3px; color: var(--ink-soft);
  }
  .read-more {
    position: absolute; left: 0; top: 760px; width: 993px; text-align: center;
    font-style: italic; font-weight: 700; font-size: 16px; color: #4a4a4a;
    text-decoration: underline;
  }
  .facts-band {
    position: absolute; left: 0; top: 801px; width: 993px; height: 203px;
    background: var(--band);
    border-top: 1px solid var(--band-edge); border-bottom: 1px solid var(--band-edge);
  }
  .fact { position: absolute; top: 27px; width: 240px; text-align: center; }
  .fact svg { display: block; margin: 0 auto 10px; }
  .fact p { font-style: italic; font-size: 16px; line-height: 20px; color: #333; }
  .fact-size { left: 238px; }
  .fact-price { left: 499px; }
  .footer-scene {
    position: absolute; left: 0; top: 1004px; width: 993px; height: 196px;
    background: linear-gradient(180deg, #f5f7f8 0%, #c7d3dc 22%, #7e96a6 40%, #8a7f6e 58%, #56633a 80%, #3e5a1f 100%);
  }
  .copyright {
    position: absolute; left: 332px; top: 1150px;
    color: var(--white); font-size: 13.5px; text-shadow: 0 1px 2px rgba(0,0,0,.5);
  }
  .follow {
    position: absolute; left: 692px; top: 1150px;
    display: flex; gap: 10px; align-items: center;
    color: var(--white); font-style: italic; font-size: 13.5px; text-shadow: 0 1px 2px rgba(0,0,0,.5);
  }
  .follow .label { text-decoration: underline; }
</style>
</head>
<body>
  <div class="sky"></div>
  <div class="phone">call us @ 000 - 555 - 0142</div>
  <div class="header-bar"></div>
  <div class="logo">LOGO</div>
  <nav class="main-nav">
    <svg width="24" height="22" viewBox="0 0 24 22" aria-label="Home"><path d="M12 2 L1 12 L4 12 L4 21 L10 21 L10 15 L14 15 L14 21 L20 21 L20 12 L23 12 Z" fill="#4a4a4a"/></svg>
    <span>APARTMENT</span>
    <span>CONDOMINIUM</span>
    <span>CONTACT US</span>
  </nav>

  <div class="signpost" role="img" aria-label="Wooden signpost on a tuft of grass reading Flat for Sale, Barra da Tijuca, Rio de Janeiro, Brazil">
    <span class="sign-sale">Flat for Sale</span>
    <span class="sign-1">Barra da Tijuca</span>
    <span class="sign-2">Rio de Janeiro</span>
    <span class="sign-3">Brazil</span>
  </div>

  <div class="gallery-main" role="img" aria-label="Photo of the penthouse living room with wooden floor and terrace"></div>
  <div class="gallery-strip">
    <svg class="arrow-btn" style="left:0" width="40" height="40" viewBox="0 0 40 40" aria-label="Previous"><circle cx="20" cy="20" r="18" fill="#fff" stroke="var(--ring)" stroke-width="3"/><path d="M24 13 L14 20 L24 27 Z" fill="#3b4a5a"/></svg>
    <div class="thumb t1" role="img" aria-label="Thumbnail of the living room"></div>
    <div class="thumb t2" role="img" aria-label="Thumbnail of the dining area"></div>
    <div class="thumb t3" role="img" aria-label="Thumbnail of the terrace pool"></div>
    <div class="thumb t4" role="img" aria-label="Thumbnail of the veranda"></div>
    <svg class="arrow-btn" style="left:385px" width="40" height="40" viewBox="0 0 40 40" aria-label="Next"><circle cx="20" cy="20" r="18" fill="#fff" stroke="var(--ring)" stroke-width="3"/><path d="M16 13 L26 20 L16 27 Z" fill="#3b4a5a"/></svg>
  </div>

  <h1 class="welcome-title">Welcome to our site</h1>
  <p class="welcome-text">Lorem ipsum dolor sit amet, consectetur adipisicing elit, sed do eiusmod tempor incididunt ut labore et dolore magna aliqua. Ut enim ad minim veniam, quis nostrud exercitation ullamco laboris nisi ut aliquip ex ea commodo consequat. Duis aute irure dolor in reprehenderit in voluptate velit esse cillum dolore eu fugiat nulla pariatur. Excepteur sint occaecat cupidatat non proident, sunt in culpa qui officia deserunt mollit anim id est laborum.</p>
  <div class="read-more">Read More...</div>

  <section class="facts-band">
    <div class="fact fact-size">
      <svg width="102" height="102" viewBox="0 0 102 102" aria-hidden="true"><circle cx="51" cy="51" r="50" fill="var(--brown)"/><circle cx="51" cy="51" r="44" fill="none" stroke="#fff" stroke-width="2" stroke-dasharray="4 3"/><path d="M51 30 L30 49 L36 49 L36 68 L46 68 L46 57 L56 57 L56 68 L66 68 L66 49 L72 49 Z" fill="#fff"/></svg>
      <p>251 SQ M<br>Duplex Penthouse, 4 suites</p>
    </div>
    <div class="fact fact-price">
      <svg width="102" height="102" viewBox="0 0 102 102" aria-hidden="true"><circle cx="51" cy="51" r="50" fill="var(--green)"/><circle cx="51" cy="51" r="44" fill="none" stroke="#fff" stroke-width="2" stroke-dasharray="4 3"/><text x="51" y="67" text-anchor="middle" font-family="Open Sans, sans-serif" font-weight="700" font-size="46" fill="#fff">$</text></svg>
      <p>Price R$ 2.200.000<br>Price per SQ M: R$ 8.764</p>
    </div>
  </section>

  <div class="footer-scene" role="img" aria-label="Aerial view of the Barra da Tijuca coastline, lagoons and green hills"></div>
  <div class="copyright">Copyright @ 2013, All rights are reserved. Company Name</div>
  <div class="follow">
    <span class="label">Follow us :</span>
    <span>Chirpline</span>
    <span>Friendwall</span>
  </div>
</body>
</html>
```